High-End audio shop owner needs a business card

I need a personal Business Card for my Audio shop which exists since 1962. We offer high Quality brands, professional Attention and run our own repair-service-department. I look for a design which will be printed on high Quality paper and shall convey trust to the Client that we are very serious. Language is german.

```html
<!DOCTYPE html>
<html lang="de">
<head>
<meta charset="utf-8">
<title>Klangwerk Adler – Visitenkarte</title>
<link rel="stylesheet" href="https://fonts.googleapis.com/css2?family=Montserrat:wght@800&family=Roboto:wght@400;500&display=swap">
<style>
  :root {
    --page: #2b2b2d;
    --card-white: #ffffff;
    --card-black: #111112;
    --orange: #f26a1b;
    --ink: #1b1b1b;
    --rule: #222222;
    --silver: #c9c9cc;
    --muted: #6e6e72;
    --edge-grey: #7d8580;
  }
  * { box-sizing: border-box; margin: 0; padding: 0; }
  html, body { width: 1200px; height: 1200px; overflow: hidden; }
  body {
    background: var(--page);
    font-family: "Roboto", Arial, sans-serif;
    position: relative;
  }
  .card {
    position: absolute;
    left: 150px;
    width: 900px;
    height: 514px;
    border-radius: 26px;
    overflow: hidden;
  }
  /* Back side */
  .card--back {
    top: 40px;
    background: var(--card-black);
  }
  .card--back .brand {
    position: absolute;
    top: 205px;
    left: 0; right: 0;
    text-align: center;
    font-family: "Montserrat", Arial, sans-serif;
    font-weight: 800;
    font-size: 56px;
    letter-spacing: 1px;
    color: var(--silver);
  }
  .card--back .web {
    position: absolute;
    bottom: 60px;
    left: 0; right: 0;
    text-align: center;
    font-size: 20px;
    font-weight: 500;
    color: var(--muted);
    letter-spacing: 0.5px;
  }
  /* Front side */
  .card--front {
    top: 626px;
    background: var(--card-white);
  }
  .card--front .brand {
    position: absolute;
    top: 58px;
    left: 62px;
    font-family: "Montserrat", Arial, sans-serif;
    font-weight: 800;
    font-size: 46px;
    color: var(--orange);
  }
  .person {
    position: absolute;
    top: 262px;
    left: 62px;
    width: 520px;
  }
  .person__name {
    font-family: "Montserrat", Arial, sans-serif;
    font-weight: 800;
    font-size: 34px;
    color: var(--ink);
    letter-spacing: 0.5px;
    padding-bottom: 10px;
    border-bottom: 2px solid var(--rule);
  }
  .contacts {
    list-style: none;
    margin-top: 10px;
  }
  .contacts li {
    display: flex;
    align-items: center;
    gap: 14px;
    font-size: 22px;
    color: var(--ink);
    line-height: 34px;
  }
  .contacts svg { width: 20px; height: 20px; flex: none; }
  .role {
    position: absolute;
    top: 312px;
    right: 62px;
    width: 380px;
    text-align: right;
  }
  .role__title {
    font-size: 26px;
    font-weight: 500;
    color: var(--orange);
    letter-spacing: 1px;
    padding-bottom: 8px;
    border-bottom: 2px solid var(--orange);
  }
  .role__address {
    margin-top: 10px;
    font-size: 22px;
    line-height: 32px;
    color: var(--ink);
  }
  .edge-line {
    position: absolute;
    left: 0; right: 0;
    bottom: 34px;
    height: 4px;
    background: var(--orange);
  }
  .edge-band {
    position: absolute;
    left: 0; right: 0;
    bottom: 0;
    height: 26px;
    background: var(--edge-grey);
  }
</style>
</head>
<body>
  <section class="card card--back" aria-label="Rückseite">
    <div class="brand">Klangwerk Adler</div>
    <div class="web">www.klangwerkadler.com</div>
  </section>

  <section class="card card--front" aria-label="Vorderseite">
    <div class="brand">Klangwerk Adler</div>

    <div class="person">
      <div class="person__name">LUKAS BRENNER</div>
      <ul class="contacts">
        <li>
          <svg viewBox="0 0 24 24" aria-hidden="true"><path fill="#f26a1b" d="M6.6 10.8a15 15 0 0 0 6.6 6.6l2.2-2.2a1 1 0 0 1 1-.25 11.4 11.4 0 0 0 3.6.57 1 1 0 0 1 1 1V20a1 1 0 0 1-1 1A17 17 0 0 1 3 4a1 1 0 0 1 1-1h3.5a1 1 0 0 1 1 1c0 1.25.2 2.45.57 3.57a1 1 0 0 1-.25 1z"/></svg>
          813-555-0147
        </li>
        <li>
          <svg viewBox="0 0 24 24" aria-hidden="true"><rect x="2" y="5" width="20" height="14" rx="1" fill="#f26a1b"/><path d="M2.5 6l9.5 7 9.5-7" fill="none" stroke="#fff" stroke-width="1.6"/></svg>
          l.brenner@klangwerkadler.com
        </li>
        <li>
          <svg viewBox="0 0 24 24" aria-hidden="true"><g fill="none" stroke="#f26a1b" stroke-width="1.8"><circle cx="12" cy="12" r="9.5"/><ellipse cx="12" cy="12" rx="4.2" ry="9.5"/><path d="M2.5 12h19M4 7h16M4 17h16"/></g></svg>
          www.klangwerkadler.com
        </li>
      </ul>
    </div>

    <div class="role">
      <div class="role__title">MANAGING PARTNER</div>
      <div class="role__address">4510 Linden Avenue, Suite 210<br>Tampa, FL 33614</div>
    </div>

    <div class="edge-line"></div>
    <div class="edge-band"></div>
  </section>
</body>
</html>
```